Wordpress Design Project

WHO WE ARE:
Bright Path Web Growth is not just another SEO or PPC company. We work with our clients to help them grow their business and achieve their goals. Our commitment to doing what is best for the customer, is why we have grown so quickly. We believe our business is not about advertising BUT about connecting customers & growing our clients businesses. We see our product as helping people, not selling a product.

PROJECT OVERVIEW:
I need to create a wordpress website for my business, www.brightpathwebgrowth.com.au

I need a whole new site created showing all of my services. The services include:
NOTE: These are not the main focus of the home page.

Consulting & Strategy Planning
Search Engine Optimisation
Pay Per Click
Re-Marketing

Once I have selected the top home page design, I will need a product and blog page designed.

SITE DESIGN:
If I was to explain the kind of style I am looking for, it would be high-street, New York agency look, web 2.0. Clean, elegant, stylish, high quality and simple looking. Kind of like you would expect from an quince website.

Think of car advertising, the closest to the target market & look/feel Im looking for would be Ravenmotor, Korel, Tamar, Brandin, Zepra.

However, I am open to any design style.

DO NOT let this restrict your creativity BUT here are some websites I like the look of.

Home page:
http://www.layoutfoundry.example/demo/52816.html
https://www.vantorix.example/intl/en/halo/devices/
http://www.vantorix.example/intl/en/halo/devices/features-different.html
http://www.layoutfoundry.example/demo/47190.html
https://www.vantorix.example/intl/en/halo/browser/features.html

Product Page:
http://www.vantorix.example/intl/en/halo/devices/buynow.html#instore

NOTE: I just added a file called "I like this color scheme.png" you can play around with something like this as well.
Updates

Please do not use the content from my current website. That is for a PPC service, the new site is for an full service agency.

Also, the message/tagline is the feature or most prominent element of the website..... Not the services we offer, these are secondary.

Great designs so far everyone, but I think I'm looking a little simpler and less crowded.  Closer to the sample sites I sent.... keep em coming.

Also, I would prefer that the 4 services, do not visually over power the tag line.  The 4 services are not important to the home page.

Lets make this easy, since every design I receive is almost the same...

Make the design look something like these 2 websites.
https://www.vantorix.example/intl/en/halo/browser/features.html#simplicity

Target Market(s)

Business Owners and entreprenuers who are well established, typically in the 35-60 year old range and spend 100k-1m in advertising per year. They big brands that target these people are Ravenmotor, Korel, Tamar, Brandin, Zepra, this should give you the feel for what I am after.

Industry/Entity Type

Advertising

Requirements
Must have
• 1. Navigations: Home, Services, About Us, Blog, Contact Us

2. The main home page words should be.... "We Grow Your Business Online" and "Clear Aim, Clear Plan, Clear Team, Bright Path Web Growth" (should use logo for last one)
I would like to see this tagline somewhere in the site "We Don't Want to be the Biggest, Just the Best!"

3. Product page must have a contact form with (name, email, phone, website)
This form must show an offer of "Free Strategy Sessions, Double your website leads", I have included an image to show as an example for the lead form "lead form example.png", see attached.

Nice to have
• I would like to see 1 or 2 of these idea's in the design.

1. I have attached some logos for Bidlane & Metricove certifications + Web association logo you can use for design purposes.

2. You can put company logo's in the design and I can change them to my clients logos at a later date.

3. Testimonials

4. Since our business is about people, pictures of people like business owners, customers using technology such as an slate, or anything like that would be good. However, is not necessary. Some idea: http://www.peerlattice.example/advertising
Should not have
• There will be no video on the design.

```html
<!DOCTYPE html>
<html lang="en">
<head>
<meta charset="utf-8">
<title>Bright Path Web Growth</title>
<link href="https://fonts.googleapis.com/css2?family=Lato:wght@300;400;700&family=Open+Sans:wght@400;600&display=swap" rel="stylesheet">
<style>
:root{
  --blue:#2f77c4;
  --blue-dark:#1f5ea8;
  --sky:#3fa9e0;
  --green:#6cb33f;
  --ink:#333;
  --muted:#777;
  --faint:#a9a9a9;
  --line:#e6e6e6;
  --band:#f7f7f7;
  --dark:#3b4043;
  --dark-text:#b9bdbf;
}
*{box-sizing:border-box;margin:0;padding:0}
html,body{width:787px;height:1200px;overflow:hidden;background:#fff}
body{position:relative;font-family:"Open Sans",Arial,sans-serif;color:var(--ink)}
.abs{position:absolute}

/* header */
.header{left:0;top:0;width:787px;height:73px;border-bottom:1px solid var(--line)}
.brand{left:101px;top:21px;display:flex;align-items:center;gap:8px}
.brand-mark{width:28px;height:28px;border-radius:50%;background:var(--blue)}
.brand-name{font-family:"Lato",sans-serif;font-weight:700;font-size:19px;color:#444;letter-spacing:-.3px;line-height:1}
.social{left:590px;top:19px;display:flex;gap:3px}
.social span{width:18px;height:18px;border-radius:50%;background:#c4c4c4;display:block}
.nav{left:392px;top:50px;display:flex;font-family:"Lato",sans-serif;font-size:10px;color:#555;letter-spacing:.3px}
.nav a{display:block;padding:0 12px;border-left:1px solid var(--line);color:inherit;text-decoration:none;line-height:14px}
.nav a:first-child{border-left:0}
.nav a.active{color:var(--ink);position:relative}
.nav a.active:after{content:"";position:absolute;left:0;right:0;top:21px;height:2px;background:var(--sky)}

/* hero */
.hero{left:0;top:74px;width:787px;height:271px;background:linear-gradient(90deg,#fff 0%,#fbfbfb 45%,#eef1f3 100%)}
.hero-photo{left:393px;top:74px;width:317px;height:271px;background:linear-gradient(90deg,#fbfbfb 0%,rgba(251,251,251,0) 35%),linear-gradient(160deg,#eef0f2 0%,#d9dcdf 45%,#3a3d40 100%)}
.call{left:533px;top:74px;width:153px;height:22px;background:var(--green);color:#fff;font-size:10px;display:flex;align-items:center;gap:8px;padding-left:10px}
.headline{left:123px;top:146px;font-family:"Lato",sans-serif;font-weight:300;font-size:28px;line-height:28px;color:#333}
.tagline{left:126px;top:212px;font-family:"Lato",sans-serif;font-size:9.6px;color:#555}
.cta{left:124px;top:238px;width:171px;height:22px;border-radius:11px;background:linear-gradient(#3c8ad6,var(--blue-dark));color:#fff;font-family:"Lato",sans-serif;font-weight:700;font-size:9.5px;letter-spacing:.4px;display:flex;align-items:center;justify-content:center}

/* services */
.services{left:0;top:345px;width:787px;height:158px;background:var(--band)}
.service{position:absolute;top:30px;width:126px}
.service-head{display:flex;align-items:center;gap:8px;height:28px}
.service-title{font-family:"Lato",sans-serif;font-size:12px;line-height:13px;color:#333;white-space:nowrap}
.service p{font-size:8.2px;line-height:10.5px;color:#777;margin-top:8px}
.service .more{font-size:8px;color:var(--sky);font-style:italic;margin-top:8px;display:block}

/* who we are */
.who{left:0;top:503px;width:787px;height:146px;background:var(--dark)}
.who h2{position:absolute;left:101px;top:22px;font-family:"Lato",sans-serif;font-weight:300;font-size:21px;color:#eee}
.who p{position:absolute;left:101px;top:50px;width:400px;font-family:"Lato",sans-serif;font-size:10px;line-height:13.6px;color:var(--dark-text)}
.who blockquote{position:absolute;left:547px;top:43px;font-family:"Lato",sans-serif;font-weight:300;font-size:16px;line-height:20px;color:#f2f2f2}
.quote-mark{position:absolute;left:520px;top:20px;font-family:Georgia,serif;font-size:110px;line-height:1;color:#454a4d}

/* why choose */
.section-title{font-family:"Lato",sans-serif;font-weight:300;font-size:17px;color:#333}
.why{left:101px;top:694px;width:165px}
.why ul{list-style:none;margin-top:8px}
.why li{display:flex;align-items:center;gap:8px;height:23.6px;border-top:1px solid #f0f0f0;font-size:9px;color:#666}
.why li:first-child{border-top:1px solid var(--line)}

/* testimonials */
.say{left:312px;top:694px}
.testimonial{position:absolute;top:731px;width:170px;height:160px}
.t-photo{position:absolute;left:0;top:0;width:30px;height:30px;background:linear-gradient(#bfbfbf,#777)}
.t-name{position:absolute;left:38px;top:0;font-family:"Lato",sans-serif;font-size:10.5px;line-height:11px;color:#333}
.t-role{position:absolute;left:38px;font-size:6.5px;line-height:8.5px;color:#999}
.t-quote{position:absolute;left:0;top:46px;font-size:8.2px;line-height:13.6px;color:#555}
.t-client{position:absolute;left:0;top:142px;font-family:"Lato",sans-serif;font-size:11px;color:#666;letter-spacing:.5px}

/* clients */
.clients{left:101px;top:934px;width:586px;height:30px;display:flex;justify-content:space-between;align-items:center}
.client{display:flex;align-items:center;gap:5px;font-family:"Lato",sans-serif;font-weight:700;font-size:15px;color:#444}
.client i{display:block;width:20px;height:20px;border-radius:50%}
.rule{left:101px;top:978px;width:586px;height:1px;background:var(--line)}

/* footer */
.footer-label{font-family:"Lato",sans-serif;font-size:7.5px;letter-spacing:.5px;color:#555}
.links{font-size:7.2px;line-height:15px;color:#555;list-style:none}
.links li:before{content:"• ";color:var(--sky)}
.divider{left:393px;top:1003px;width:1px;height:128px;background:var(--line)}
.map{left:540px;top:1023px;width:135px;height:78px;background:radial-gradient(ellipse at center,#e6e6e6 0%,#f2f2f2 60%,#fff 100%)}
.phone{left:419px;top:1031px;font-family:"Lato",sans-serif;font-size:12px;color:var(--green)}
.address{left:421px;top:1053px;font-size:8.5px;line-height:11px;color:#999}
.contact-line{font-size:7.5px;color:#888;display:flex;align-items:center;gap:6px}
.signup{left:101px;top:1107px;display:flex}
.signup .field{width:124px;height:18px;border:1px solid #ddd;font-size:7.5px;color:#aaa;padding:4px 6px}
.signup .btn{width:57px;height:18px;background:var(--green);color:#fff;font-size:8.5px;display:flex;align-items:center;justify-content:center}
.copy{left:101px;top:1131px;font-size:6.8px;color:#666}
</style>
</head>
<body>

<header class="abs header">
  <div class="abs brand"><span class="brand-mark"></span><span class="brand-name">Bright Path Web Growth</span></div>
  <div class="abs social"><span></span><span></span><span></span><span></span><span></span></div>
  <nav class="abs nav">
    <a class="active">HOME</a><a>SERVICES</a><a>ABOUT US</a><a>BLOG</a><a>CONTACT US</a>
  </nav>
</header>

<section class="abs hero"></section>
<div class="abs hero-photo" role="img" aria-label="Photo of a smiling businesswoman using a slate in a bright office"></div>
<div class="abs call">
  <svg width="10" height="10" viewBox="0 0 10 10"><path d="M2 1l2 2-1 1.3c.6 1.2 1.5 2.1 2.7 2.7L7 6l2 2-1.3 1.3C4.5 9 1 5.5.7 2.3z" fill="#fff"/></svg>
  <span>Call us: (020) 5160 2947</span>
</div>
<h1 class="abs headline">We Grow Your<br>Business Online</h1>
<p class="abs tagline">Clear Aim, Clear Plan, Clear Team, Bright Path Web Growth</p>
<div class="abs cta">GET A FREE SEO REVIEW &nbsp;»</div>

<section class="abs services">
  <div class="service" style="left:101px">
    <div class="service-head"><svg width="16" height="12" viewBox="0 0 16 12"><path d="M1 2l7 2 7-2v9l-7 1-7-1z" fill="none" stroke="#3fa9e0" stroke-width="1.4"/></svg><span class="service-title">Consulting &amp;<br>Strategy Planning</span></div>
    <p>We built Apps not only to be faster, but also to put you in otect the information you share when you're online.</p>
    <span class="more">Read more →</span>
  </div>
  <div class="service" style="left:247px">
    <div class="service-head"><svg width="14" height="14" viewBox="0 0 14 14"><path d="M2 2h10M5 5h7M5 8h7M5 11h7" stroke="#3fa9e0" stroke-width="1.5"/></svg><span class="service-title">Search Engine<br>Optimisation (SEO)</span></div>
    <p>We built Apps not only to be faster, but also to put you in otect the information you share when you're online.</p>
    <span class="more">Read more →</span>
  </div>
  <div class="service" style="left:397px">
    <div class="service-head"><svg width="12" height="16" viewBox="0 0 12 16"><circle cx="6" cy="5" r="3.5" fill="none" stroke="#3fa9e0" stroke-width="1.4"/><path d="M6 8v7" stroke="#3fa9e0" stroke-width="1.6"/></svg><span class="service-title">Pay Per Click (PPC)</span></div>
    <p>We built Apps not only to be faster, but also to put you in otect the information you share when you're online.</p>
    <span class="more">Read more →</span>
  </div>
  <div class="service" style="left:543px">
    <div class="service-head"><svg width="22" height="12" viewBox="0 0 22 12"><circle cx="5" cy="4" r="2.5" fill="#3fa9e0"/><circle cx="11" cy="3.5" r="3" fill="#3fa9e0"/><circle cx="17" cy="4" r="2.5" fill="#3fa9e0"/><path d="M1 12c0-4 8-4 8 0M6 12c0-5 10-5 10 0M13 12c0-4 8-4 8 0" fill="#3fa9e0"/></svg><span class="service-title">Re-Marketing</span></div>
    <p>We built Apps not only to be faster, but also to put you in otect the information you share when you're online.</p>
    <span class="more">Read more →</span>
  </div>
</section>

<section class="abs who">
  <h2>Who We Are</h2>
  <p>Bright Path Web Growth is not just another SEO or PPC company. We work with our clients to help them grow their business and achieve their goals. Our commitment to doing what is best for the customer, is why we have grown so quickly Bright Path Web Growth is not just another SEO or PPC company. We work to doing what is best for the customer, is why we have grown so quickly.</p>
  <span class="quote-mark">“</span>
  <blockquote>“We Don't Want<br>to be the Biggest,<br>Just the Best!”</blockquote>
</section>

<section class="abs why">
  <h2 class="section-title">Why choose us?</h2>
  <ul>
    <li><svg width="8" height="7" viewBox="0 0 8 7"><path d="M1 3.5l2 2L7 1" fill="none" stroke="#999" stroke-width="1.5"/></svg>SEO Optimized</li>
    <li><svg width="8" height="7" viewBox="0 0 8 7"><path d="M1 3.5l2 2L7 1" fill="none" stroke="#999" stroke-width="1.5"/></svg>Colorpick each element</li>
    <li><svg width="8" height="7" viewBox="0 0 8 7"><path d="M1 3.5l2 2L7 1" fill="none" stroke="#999" stroke-width="1.5"/></svg>Background uploader</li>
    <li><svg width="8" height="7" viewBox="0 0 8 7"><path d="M1 3.5l2 2L7 1" fill="none" stroke="#999" stroke-width="1.5"/></svg>Widgitized Homepage</li>
    <li><svg width="8" height="7" viewBox="0 0 8 7"><path d="M1 3.5l2 2L7 1" fill="none" stroke="#999" stroke-width="1.5"/></svg>Solid and clean code</li>
    <li><svg width="8" height="7" viewBox="0 0 8 7"><path d="M1 3.5l2 2L7 1" fill="none" stroke="#999" stroke-width="1.5"/></svg>Ongoing support</li>
  </ul>
</section>

<h2 class="abs section-title say">What People Say</h2>

<article class="testimonial" style="left:312px">
  <div class="t-photo" role="img" aria-label="Portrait photo of the client"></div>
  <div class="t-name">Tomas<br>Lindqvar</div>
  <div class="t-role" style="top:26px">Director Velmora</div>
  <p class="t-quote">"We are delighted to work with the team Bright Path our SEO strategy for their demonstrated professionalism and accomplishment. Notably adequacy SEO planning to the particularities of our markets."</p>
  <div class="t-client">VELMORA</div>
</article>

<article class="testimonial" style="left:513px">
  <div class="t-photo" role="img" aria-label="Portrait photo of the client"></div>
  <div class="t-name">Arun<br>Deshvel</div>
  <div class="t-role" style="top:26px">Customer Experience and Social<br>Media Manager at Quellion</div>
  <p class="t-quote" style="top:57px">"We are delighted to work with the team Bright Path our SEO strategy for their demonstrated professionalism and accomplishment. Notably adequacy SEO planning to the particularities of our markets."</p>
  <div class="t-client" style="top:147px">quellion</div>
</article>

<div class="abs clients">
  <span class="client"><i style="background:#3fa9e0"></i>Strivo</span>
  <span class="client"><i style="background:#e0564f"></i>Kelto</span>
  <span class="client"><i style="background:#555"></i>Parcelyn</span>
  <span class="client"><i style="background:#7fb43b"></i>Notion Hale</span>
  <span class="client"><i style="background:#2cc3ea;width:28px;height:28px"></i></span>
  <span class="client"><i style="background:#f2a93b"></i>Cobalta</span>
</div>
<div class="abs rule"></div>

<div class="abs footer-label" style="left:101px;top:1009px">QUICK LINKS</div>
<ul class="abs links" style="left:101px;top:1021px">
  <li>Consulting &amp; Strategy Planning</li><li>Search Engine Optimisation (SEO)</li><li>Pay Per Click (PPC)</li><li>Re-Marketing</li>
</ul>
<ul class="abs links" style="left:248px;top:1021px"><li>Home</li><li>Services</li><li>About Us</li></ul>
<ul class="abs links" style="left:311px;top:1021px"><li>Blog</li><li>Contact Us</li></ul>
<div class="abs footer-label" style="left:101px;top:1094px">STAY UP TO DATE</div>
<div class="abs signup"><div class="field">user@mailbox.example</div><div class="btn">SIGNUP</div></div>
<div class="abs copy">Copyright © 2012 Bright Path Web Growth®</div>

<div class="abs divider"></div>
<div class="abs map" role="img" aria-label="Faint world map"></div>
<div class="abs footer-label" style="left:419px;top:1009px">GET IN TOUCH</div>
<div class="abs phone">(020) 5160 2948</div>
<div class="abs address">41 Harlow Lane Suite<br>310 Marden NY 10290</div>
<div class="abs contact-line" style="left:421px;top:1085px"><svg width="8" height="6" viewBox="0 0 8 6"><rect width="8" height="6" fill="#aaa"/><path d="M0 0l4 3 4-3" stroke="#fff" fill="none"/></svg>support@brightpathgrowth.example</div>
<div class="abs contact-line" style="left:421px;top:1099px"><svg width="6" height="8" viewBox="0 0 6 8"><path d="M3 8C1 5 0 4 0 3a3 3 0 016 0c0 1-1 2-3 5z" fill="#aaa"/></svg>Get directions</div>

</body>
</html>
```